Online Prescription Eyeglass Lens Company Needs a Website

*Update new name to Glintwell. Thx

We are eye doctors with a lab that need a website for a new company based in Southern California called Glintwell. We replace old prescription lenses with new ones next day for most lenses. Patients select the lenses and give us the prescription. We then send a box with a prepaid shipping label. Place the frames in the box and drop them in the mail to our lab. We will custom make new lenses, fit them back into your frames and send them back to you. We would like to compete with www.spectrafold.com and offer affordable lenses for single vision, bifocal, progressive, sunglass lenses at an affordable price with next day shipping.
Updates

Hi Designers, We have a new name called Glintwell. Can we have the website design reflect the new name and we'll pick our favorites. Thx

Update: The new name is Brightmoor . I have not made very many changes or feedback to the submissions because we were bidding for a .com. We won and our new name is Brightmoor . This is the last name change.. Please have the website reflect the new name and I'll be providing feedback on the websites . ( I have a separate project for the logo people are working on, so don't worry about creating a logo). Look forward to the submissions. Thanks everyone.

Hi, Just leave the name as Glintwell for now. I will narrow down top designs tonight. Thx

Target Market(s)

Anyone that wears prescription or nonprescription glasses or sunglasses that want next day shipping.

Industry/Entity Type

Eyewear

Number of Pages Required

4 page

Font styles to use
Serif

Colors

Designer to choose colors to be used in the design.

Requirements
Must have
• I need a website that can compete with https://www.spectrafold.com/.
• We are different from spectrafold because we can offer same day service or next day shipping.
• It needs to have website that offers the lenses available listed below.
• Needs to be able to upload a prescription and payment feature.
• Pictures of different types of options with small info about each lens option.
• Template Pricing (just use numbers from $79-$179 for now)
• SINGLE VISION LENSES
• HIGH INDEX LENSES
• READING LENSES
• DIGITAL HD PROGRESSIVE LENSES
• RX & NON-RX SUNGLASSES
• RX & NON-RX POLARIZED SUNGLASSES
• COMPUTER LENSES
• TRANSITION LENSES
• BI-FOCAL LENSES

```html
<!DOCTYPE html>
<html lang="en">
<head>
<meta charset="utf-8">
<title>Glintwell — Our Lenses, Your Specs</title>
<link rel="stylesheet" href="https://fonts.googleapis.com/css2?family=Roboto:wght@300;400;500;700&family=Roboto+Slab:wght@400;500&family=Open+Sans:wght@400;600&display=swap">
<style>
:root{
  --ink:#222230;
  --muted:#555862;
  --paper:#f4f4f4;
  --white:#ffffff;
  --night:#1f1d2c;
  --night-soft:#2c2a3a;
  --yellow:#f7c531;
  --pale-blue:#cfe6f4;
  --quote-blue:#bfe2f3;
  --magenta:#a3284f;
  --teal:#3f8f7e;
  --violet:#5a4de2;
  --gold:#9a6710;
  --red:#b62a37;
  --line:#c9c9c9;
}
*{margin:0;padding:0;box-sizing:border-box}
html,body{width:1200px;height:3704px;overflow:hidden}
body{position:relative;background:var(--paper);font-family:"Open Sans",Arial,sans-serif;color:var(--ink)}
.abs{position:absolute}

/* hero */
.hero{position:absolute;left:0;top:0;width:1200px;height:723px;overflow:hidden;
  background:radial-gradient(circle at 20% 30%,#4a3a30 0,#241d1d 45%,#15131a 100%)}
.hero-photo{position:absolute;left:605px;top:0;width:595px;height:723px;
  background:linear-gradient(180deg,#2a2422 0%,#3a2a2a 40%,#a98425 75%,#c89a22 100%)}
.brand{position:absolute;display:flex;align-items:center;gap:10px;font-family:"Roboto",sans-serif;font-weight:500;color:var(--white)}
.brand-dot{width:30px;height:30px;border-radius:50%;background:#58c3ee}
.hero .brand{left:160px;top:48px;font-size:30px}
.nav{position:absolute;top:62px;left:0;width:1200px;font-family:"Roboto",sans-serif;font-size:12px;font-weight:500;color:var(--white);letter-spacing:.5px}
.nav span{position:absolute;white-space:nowrap}
.nav .order{left:889px;top:-18px;width:148px;height:50px;border:1.5px solid rgba(255,255,255,.8);border-radius:25px;display:flex;align-items:center;justify-content:center}
.hero-title{position:absolute;left:154px;top:186px;font-family:"Roboto",sans-serif;font-weight:300;font-size:74px;line-height:94px;color:var(--white);letter-spacing:1px}
.hero-title b{font-weight:700}
.hero-sub{position:absolute;left:158px;top:372px;font-family:"Roboto",sans-serif;font-size:12px;line-height:20px;letter-spacing:4px;color:#e8e8e8}
.price-label{position:absolute;left:160px;top:500px;font-family:"Roboto",sans-serif;font-size:19px;color:var(--white)}
.price{position:absolute;left:277px;top:485px;width:82px;height:50px;background:var(--yellow);display:flex;align-items:center;justify-content:center;font-family:"Roboto",sans-serif;font-weight:700;font-size:26px;color:var(--ink)}
.pill{position:absolute;height:54px;border-radius:27px;background:var(--white);display:flex;align-items:center;justify-content:center;font-family:"Roboto",sans-serif;font-weight:500;font-size:12px;letter-spacing:3px;color:var(--ink)}

/* process */
.section-title{position:absolute;left:0;width:1200px;text-align:center;font-family:"Roboto Slab",serif;font-weight:400;font-size:40px}
.rule{position:absolute;height:6px;border-top:1.5px solid var(--line);border-bottom:1.5px solid var(--line)}
.intro{position:absolute;left:300px;width:600px;text-align:center;font-size:13px;line-height:27px;color:var(--muted)}
.step-num{position:absolute;font-family:"Roboto",sans-serif;font-weight:300;font-size:124px;line-height:1;color:var(--pale-blue)}
.step-title{position:absolute;font-family:"Roboto",sans-serif;font-weight:400;font-size:40px;line-height:48px;color:var(--ink);white-space:nowrap}
.step-text{position:absolute;font-size:13px;line-height:27px;color:var(--muted)}
.art{position:absolute;border-radius:18px}
.refer{position:absolute;font-family:"Roboto",sans-serif;font-size:22px;color:var(--red)}

/* lab */
.lab{position:absolute;left:0;top:2291px;width:1200px;height:331px;background:linear-gradient(120deg,#3a3848 0%,#23212f 50%,#2f2d3c 100%)}
.lab .section-title{color:var(--white);top:60px}
.lab p{position:absolute;left:0;top:137px;width:1200px;text-align:center;font-size:13px;color:#e0e0e6}

/* testimonials */
.testi-photo{position:absolute;left:0;top:2622px;width:610px;height:484px;background:linear-gradient(135deg,#d9dde2 0%,#9aa0a8 45%,#5c5a5e 100%)}
.testi{position:absolute;left:610px;top:2622px;width:590px;height:484px;background:var(--white)}
.quote-mark{position:absolute;font-family:"Roboto Slab",serif;font-size:110px;line-height:1;color:var(--quote-blue)}

/* newsletter */
.join{position:absolute;left:0;top:3106px;width:1200px;height:331px;background:linear-gradient(110deg,#3b3337 0%,#4a3e38 40%,#2a2530 100%)}
.join .section-title{color:var(--white);top:66px}
.join .lead{position:absolute;left:0;top:144px;width:1200px;text-align:center;font-family:"Roboto",sans-serif;font-weight:500;font-size:22px;color:var(--white)}
.field{position:absolute;left:321px;top:217px;width:558px;height:50px;border-radius:25px;background:var(--white);display:flex;align-items:center;padding-left:30px;font-size:12px;letter-spacing:2px;color:#777}
.submit{position:absolute;right:0;top:0;width:148px;height:50px;border-radius:25px;background:var(--yellow);display:flex;align-items:center;justify-content:center;letter-spacing:2px;color:var(--ink)}

/* footer */
.footer{position:absolute;left:0;top:3437px;width:1200px;height:267px;background:var(--night)}
.footer .brand{left:162px;top:42px;font-size:30px}
.footer .about-text{position:absolute;left:168px;top:100px;width:210px;font-size:13px;line-height:19px;color:var(--white)}
.col-head{position:absolute;top:48px;font-size:11px;font-weight:600;letter-spacing:3px;color:var(--yellow)}
.links{position:absolute;top:92px;list-style:none;font-size:13px;line-height:23px;color:var(--white)}
.social{position:absolute;left:889px;top:108px;display:flex;gap:18px}
.social span{width:20px;height:20px;border-radius:50%;background:var(--white)}
.copy{position:absolute;left:790px;top:196px;font-size:11px;color:var(--white)}
</style>
</head>
<body>

<header class="hero">
  <div class="hero-photo" role="img" aria-label="Photo of a smiling woman in glasses and a yellow cardigan holding a pen"></div>
  <div class="brand"><span class="brand-dot"></span>Glintwell</div>
  <nav class="nav">
    <span style="left:375px">OUR LENSES</span>
    <span style="left:484px">WHY GLINTWELL</span>
    <span style="left:600px">THE LAB</span>
    <span style="left:686px">OUR PROCESS</span>
    <span style="left:812px">SIGN IN</span>
    <span class="order">ORDER LENSES</span>
  </nav>
  <h1 class="hero-title">OUR <b>LENSES,</b><br><b>YOUR</b> SPECS.</h1>
  <p class="hero-sub">GET THE LENSES YOU NEED,<br>IN YOUR OWN FRAMES, WITHOUT LEAVING HOME</p>
  <span class="price-label">Starting at</span>
  <span class="price">$77</span>
  <a class="pill" style="left:156px;top:585px;width:256px">CHOOSE YOUR LENSES</a>
</header>

<main>
  <section class="process">
    <span class="rule" style="left:296px;top:796px;width:120px"></span>
    <h2 class="section-title" style="top:770px">How We Works</h2>
    <span class="rule" style="left:784px;top:796px;width:120px"></span>
    <p class="intro" style="top:840px">A brief overview of the process that will have your new lenses delivered back at your door in around 2 weeks or less.</p>

    <div class="art" style="left:705px;top:951px;width:332px;height:321px;background:radial-gradient(circle,#f2dcd0 0,#f6eeee 55%,transparent 72%)" role="img" aria-label="Illustration of an optician surrounded by a ring of colourful glasses"></div>
    <span class="step-num" style="left:130px;top:1068px">1</span>
    <h3 class="step-title" style="left:210px;top:1070px">PICK <span style="color:var(--magenta);font-weight:500">YOUR LENSES.</span></h3>
    <p class="step-text" style="left:210px;top:1140px;width:420px">Far, near, sun, clear, Lightshift ®, and then some. This is where you give us your prescription and your preferences.</p>

    <div class="art" style="left:148px;top:1259px;width:296px;height:252px;background:linear-gradient(135deg,#f0c9a0 0%,#e3b07c 50%,#2b2b2b 100%)" role="img" aria-label="Illustration of a hand holding a smartphone showing glasses"></div>
    <h3 class="step-title" style="left:530px;top:1391px">SEND US <span style="color:var(--teal);font-weight:500">YOUR FRAMES.</span></h3>
    <span class="step-num" style="left:1005px;top:1372px">2</span>
    <p class="step-text" style="left:530px;top:1473px;width:480px">Use the prepaid, secure box we provide to send us your favorite frames.</p>

    <span class="step-num" style="left:158px;top:1715px">3</span>
    <h3 class="step-title" style="left:244px;top:1717px">WE RE LENS <span style="color:var(--violet);font-weight:500">YOUR<br>GLASSES.</span></h3>
    <p class="step-text" style="left:244px;top:1830px;width:480px">We scan your frames, cut new lenses, and fit them perfectly into your frames.</p>
    <div class="art" style="left:790px;top:1580px;width:247px;height:370px;background:linear-gradient(180deg,#f3d8c8 0%,#e9e9ec 55%,#cfcfd4 100%)" role="img" aria-label="Illustration of a lab technician in goggles holding up glasses"></div>

    <div class="art" style="left:148px;top:1963px;width:358px;height:222px;background:linear-gradient(135deg,#e2a560 0%,#c88a45 50%,#3fa6da 100%)" role="img" aria-label="Illustration of an open cardboard box and a blue delivery van"></div>
    <h3 class="step-title" style="left:548px;top:1988px;width:400px;text-align:right;line-height:62px;color:var(--gold);font-weight:500">SIGHT, SEALED,<br>DELIVERED.</h3>
    <span class="step-num" style="left:968px;top:1993px">4</span>
    <p class="step-text" style="left:508px;top:2114px;width:440px;text-align:right">Sit back and relax! We'll bring your new and improved specs directly to your door at a more affordable price. It's really that easy.</p>
    <span class="refer" style="left:797px;top:2192px">Refer and Earn.</span>
  </section>

  <section class="lab" role="img" aria-label="Darkened photo of lenses on lab equipment">
    <h2 class="section-title">Our Lab</h2>
    <p>Every lens is manufactured in our state-of-the-art, licensed lab in Los Angeles, California.</p>
    <a class="pill" style="left:472px;top:208px;width:254px">LEARN MORE ABOUT US</a>
  </section>

  <section>
    <div class="testi-photo" role="img" aria-label="Photo of a woman in blue glasses and a leather jacket"></div>
    <div class="testi">
      <h2 style="position:absolute;left:158px;top:82px;font-family:'Roboto Slab',serif;font-weight:400;font-size:40px">Testimonials</h2>
      <span class="quote-mark" style="left:62px;top:172px">&ldquo;</span>
      <p style="position:absolute;left:158px;top:176px;font-family:'Roboto',sans-serif;font-size:22px">Nora Whitfield</p>
      <p style="position:absolute;left:158px;top:212px;font-size:13px;color:#888">Marketing</p>
      <p style="position:absolute;left:158px;top:260px;width:338px;font-size:13px;line-height:27px;color:var(--muted);text-align:justify">Lorem Ipsum is simply dummy text of the printing and typesetting industry. Lorem Ipsum has been the industry's standard dummy tley of type and scrambled Ipsum.</p>
      <span class="quote-mark" style="left:468px;top:362px">&rdquo;</span>
    </div>
  </section>

  <section class="join" role="img" aria-label="Dim photo of friends in sunglasses outdoors">
    <h2 class="section-title">Join The Family</h2>
    <p class="lead">Subscribe to stay up to date with weekly specials and subscriber exclusives.</p>
    <div class="field">Enter your mail<span class="submit">Submit</span></div>
  </section>
</main>

<footer class="footer">
  <div class="brand"><span class="brand-dot"></span>Glintwell</div>
  <p class="about-text">Lorem Ipsum is simply dummy text of the printing and typesetting industry. Lorem Ipsum has been the industry's</p>
  <span class="col-head" style="left:462px">ABOUT</span>
  <ul class="links" style="left:462px"><li>Why Spectrafold</li><li>Our Process</li><li>Our Lab</li><li>Refer a Friend</li><li>Blog</li></ul>
  <span class="col-head" style="left:679px">SUPPORT</span>
  <ul class="links" style="left:679px"><li>Track Order</li><li>Contact</li><li>FAQs</li><li>Returns</li><li>Terms</li></ul>
  <span class="col-head" style="left:889px">FOLLOW US</span>
  <div class="social"><span></span><span></span><span></span><span></span></div>
  <p class="copy">Copyright © 2017 Glintwell.com. All rights reserved.</p>
</footer>

</body>
</html>
```